The tooth corner of brimwell web page

website for dental office
Already have domain, mostly information only with address, telephone and google map and hours of operation on top. mobile friendly. SEO a most.

Target Market(s)

Local families

Industry/Entity Type

Dental Clinic

Number of Pages Required

1 page

Font styles to use
Serif

Colors

Designer to choose colors to be used in the design.

Requirements
Must have
• SEO
• Information to find the location
• mobile friendly
• dr's. biography
• services offered
• contect to social media (google, facebook, and instagram)
• Se habla espaƱol
• All insurance accepted
• request an appointment form to notify us

```html
<!DOCTYPE html>
<html lang="en">
<head>
<meta charset="utf-8">
<title>The Tooth Corner of Brimwell – Family Dental Clinic</title>
<meta name="description" content="Family dental clinic in Brimwell. Preventive, restorative, cosmetic and emergency dentistry. All insurance accepted. Se habla español.">
<link href="https://fonts.googleapis.com/css2?family=Montserrat:ital,wght@0,400;0,500;0,600;0,700;0,800;1,500;1,600;1,700&family=Open+Sans:ital,wght@0,400;0,600;0,700;1,400&family=Lora:ital,wght@0,600;1,400&display=swap" rel="stylesheet">
<style>
:root{
  --green:#8cc63f;
  --green-dark:#6fa82a;
  --blue:#0d4fa0;
  --blue-deep:#0a3f86;
  --text:#555;
  --muted:#8a8a8a;
  --line:#dcdcdc;
  --topbar:#f2f2f2;
  --footer:#1f1f1f;
  --footer-bottom:#141414;
  --white:#fff;
}
*{box-sizing:border-box;margin:0;padding:0}
html,body{width:1200px;height:4786px;overflow:hidden}
body{font-family:"Open Sans",Arial,sans-serif;color:var(--text);background:var(--white);position:relative}
section,header,footer{position:absolute;left:0;width:1200px}
.abs{position:absolute}
.brand-name{font-family:"Montserrat",Arial,sans-serif;font-weight:700;color:var(--blue);text-transform:uppercase;letter-spacing:.5px;line-height:1.15}
.brand-dot{display:inline-block;width:34px;height:34px;border-radius:50%;background:var(--green);vertical-align:middle;flex:none}

/* top bar */
.topbar{position:absolute;left:0;top:0;width:1200px;height:34px;background:var(--topbar);font-size:12px;color:#666}
.topbar .address{left:110px;top:9px;display:flex;gap:8px;align-items:center}
.topbar .promo{right:110px;top:9px;display:flex;gap:8px;align-items:center}
.topbar .promo b{color:#333}

/* nav */
.site-header{top:34px;height:150px;background:var(--white)}
.site-header .logo{left:110px;top:48px;display:flex;gap:12px;align-items:center}
.site-header .logo .brand-name{font-size:14px;width:190px}
.main-nav{left:395px;top:64px;display:flex;gap:34px;font:600 15px "Montserrat",sans-serif;color:#333}
.main-nav .active{color:var(--green)}
.main-nav span.caret::after{content:" ▾";font-size:10px}
.site-header .phone{left:985px;top:64px;font:700 16px "Montserrat",sans-serif;color:#333;display:flex;gap:8px;align-items:center}

/* hero */
.hero{top:188px;height:684px;background:linear-gradient(90deg,#f4f6f8 0%,#eef1f4 40%,#dfe6ec 70%,#cfd9e2 100%)}
.hero .photo{left:560px;top:0;width:640px;height:684px;background:linear-gradient(180deg,#e7ecf0,#c6d2dc)}
.hero .welcome{left:95px;top:176px;width:540px;text-align:center;font:italic 500 42px "Montserrat",sans-serif;color:#333;line-height:1.2}
.hero .brand-name{left:75px;top:240px;width:580px;text-align:center;font-size:44px;white-space:nowrap;line-height:1.1}
.hero .brand-sub{left:95px;top:294px;width:540px;text-align:center;font:600 20px "Montserrat",sans-serif;color:var(--green);letter-spacing:6px;text-transform:uppercase;line-height:1.2}
.hero .tagline{left:95px;top:338px;width:540px;text-align:center;font:500 36px "Montserrat",sans-serif;color:var(--blue);line-height:1.2}
.btn{display:inline-block;background:var(--green);color:var(--white);font:600 20px "Montserrat",sans-serif;border-radius:4px;text-align:center}
.hero .btn{left:240px;top:448px;width:250px;height:48px;line-height:48px}

/* about */
.about{top:872px;height:538px}
.about .logo{left:110px;top:128px;display:flex;gap:14px;align-items:center}
.about .logo small{display:block;font:italic 400 18px "Lora",serif;color:#444;margin-bottom:2px}
.about .logo .brand-name{font-size:20px}
.about .bio{left:110px;top:218px;width:450px;font-size:12.5px;line-height:1.75;color:var(--muted)}
.about .bio p+p{margin-top:16px}
.about .btn{left:110px;top:400px;width:125px;height:30px;line-height:30px;font-size:12px;border-radius:15px}
.hours-card{left:648px;top:128px;width:452px;height:306px;border:1px solid var(--line)}
.hours-card .photo{left:10px;top:10px;width:200px;height:238px;background:linear-gradient(180deg,#dfe7ee,#b8c8d6)}
.hours-card h3{left:228px;top:22px;font:italic 600 20px "Montserrat",sans-serif;color:var(--blue)}
.hours-card table{position:absolute;left:228px;top:66px;border-collapse:collapse;font-size:17px;color:#444}
.hours-card td{padding:6px 26px 6px 0}
.hours-card .name-bar{left:10px;top:258px;width:430px;height:36px;background:var(--blue);color:var(--white);font:600 15px "Montserrat",sans-serif;text-align:center;line-height:36px}

/* banner */
.banner{top:1410px;height:512px;background:linear-gradient(90deg,#e9eef2 0%,#dfe7ee 50%,#e6ecf1 100%)}
.banner .photo{left:0;top:0;width:580px;height:512px;background:linear-gradient(135deg,#e4d6c8,#c8b4a0 55%,#d8dfe6)}
.banner .heading{left:620px;top:86px;width:480px;text-align:center;font:italic 600 52px "Montserrat",sans-serif;color:var(--blue);line-height:1.12}
.banner .heading strong{font-weight:700;font-size:60px}
.call-box{left:615px;top:218px;width:485px;height:136px;background:var(--green);text-align:center;color:var(--white)}
.call-box .label{margin-top:18px;font:700 24px "Montserrat",sans-serif;color:var(--blue-deep)}
.call-box .number{font:700 56px "Montserrat",sans-serif;line-height:1.15;color:var(--blue-deep)}
.banner .touch{left:615px;top:388px;width:485px;text-align:center;font:500 24px "Montserrat",sans-serif;color:var(--blue)}
.social{display:flex;gap:10px}
.social span{width:28px;height:28px;border-radius:50%;border:2px solid currentColor;display:block}
.banner .social{left:808px;top:436px;color:var(--blue-deep)}

/* services */
.services{top:1922px;height:678px}
.section-title{width:1200px;text-align:center;font:italic 600 38px "Montserrat",sans-serif;color:var(--blue)}
.section-title em{color:var(--green)}
.services .section-title{top:86px}
.services .sub{top:140px;width:1200px;text-align:center;font:500 16px "Montserrat",sans-serif;color:#555;letter-spacing:1px}
.divider{left:390px;width:420px;height:20px}
.services .divider{top:166px}
.services .intro{left:110px;top:226px;width:980px;text-align:center;font-size:12.5px;line-height:1.75;color:var(--muted)}
.service{top:348px;width:240px;text-align:center}
.service .circle{margin:0 auto;width:112px;height:112px;border-radius:50%;background:var(--green);display:flex;align-items:center;justify-content:center}
.service h4{margin-top:28px;font:700 14px "Montserrat",sans-serif;color:var(--blue)}
.service p{margin-top:8px;font-size:12px;line-height:1.6;color:#666}

/* appointment */
.appointment{top:2600px;height:872px;background:var(--blue)}
.appointment .section-title{top:52px;color:var(--white)}
.appointment .sub{top:104px;width:1200px;text-align:center;font:500 15px "Montserrat",sans-serif;color:var(--white)}
.steps-line{left:110px;top:190px;width:980px;height:2px;background:rgba(255,255,255,.6)}
.step{top:160px;width:200px;text-align:center;color:var(--white);font:600 14px "Montserrat",sans-serif}
.step .box{margin:0 auto 28px;width:58px;height:58px;background:var(--white);border-radius:4px;display:flex;align-items:center;justify-content:center}
.form-card{left:125px;top:325px;width:965px;height:445px;background:var(--white);border-top:8px solid var(--green)}
.form-card .field{position:absolute;height:34px;background:#f0f0f0;border:1px solid #e0e0e0;font:italic 13px "Open Sans",sans-serif;color:#999;padding:0 10px;line-height:32px;white-space:nowrap;overflow:hidden}
.form-card .note{left:95px;top:285px;font:italic 12px "Open Sans",sans-serif;color:#999}
.form-card .btn{left:92px;top:325px;width:788px;height:36px;line-height:36px;font-size:15px;border-radius:2px}

/* testimonials */
.testimonials{top:3472px;height:478px;background:linear-gradient(180deg,#6f9fc4 0%,#4f86b3 60%,#5e90b9 100%)}
.testimonials .section-title{top:60px;color:var(--white);font-style:normal}
.testimonials .quote{left:110px;top:160px;width:980px;text-align:center;font-size:12.5px;line-height:1.75;color:rgba(255,255,255,.9)}
.testimonials .author{top:280px;width:1200px;text-align:center;font:700 13px "Montserrat",sans-serif;color:var(--white);letter-spacing:1px}
.avatars{left:440px;top:312px;display:flex;gap:20px}
.avatars span{width:60px;height:60px;border-radius:50%;border:3px solid var(--white);background:linear-gradient(135deg,#e6c9b1,#b8937a);display:block}

/* map */
.map{top:3950px;height:342px;background:linear-gradient(135deg,#e9ece4,#dde3df 50%,#e7e9e3)}

/* footer */
.site-footer{top:4292px;height:494px;background:var(--footer);color:#ccc}
.site-footer .logo{left:110px;top:80px;width:220px;text-align:center}
.site-footer .logo .brand-name{color:var(--white);font-size:19px;margin-top:12px}
.habla{left:150px;top:262px;width:110px;height:62px;border:3px solid var(--white);color:var(--white);font:800 17px "Montserrat",sans-serif;text-align:center;line-height:1.2;padding-top:8px}
.site-footer h5{font:700 17px "Montserrat",sans-serif;color:var(--green)}
.footer-contact{left:420px;top:80px;width:300px}
.footer-contact .addr{margin-top:26px;display:flex;gap:12px}
.footer-contact .addr b{display:block;color:var(--green);font:700 14px "Montserrat",sans-serif}
.footer-contact .addr p{font-size:14px;line-height:1.5}
.footer-contact .call{margin-top:28px;font:500 16px "Montserrat",sans-serif;color:var(--green)}
.footer-contact .num{font:700 28px "Montserrat",sans-serif;color:var(--white)}
.footer-doctor{left:755px;top:80px;width:340px}
.footer-doctor p{margin-top:12px;font-size:13px;line-height:1.5}
.footer-doctor .btn{margin-top:18px;width:170px;height:32px;line-height:32px;font-size:12px;color:#1d3b17}
.footer-doctor .touch{margin-top:18px;font:500 16px "Montserrat",sans-serif;color:var(--green)}
.footer-doctor .social{margin-top:6px;color:#ddd}
.footer-doctor .social span{width:24px;height:24px}
.footer-doctor .insurance{margin-top:22px;font:600 18px "Montserrat",sans-serif;color:var(--green);display:flex;gap:8px;align-items:center}
.footer-bottom{position:absolute;left:0;top:445px;width:1200px;height:49px;background:var(--footer-bottom);text-align:center;line-height:49px;font-size:12px;color:#888}
</style>
</head>
<body>

<div class="topbar">
  <div class="address abs">
    <svg width="10" height="14" viewBox="0 0 10 14"><path d="M5 0a5 5 0 0 0-5 5c0 4 5 9 5 9s5-5 5-9a5 5 0 0 0-5-5zm0 7a2 2 0 1 1 0-4 2 2 0 0 1 0 4z" fill="#777"/></svg>
    4120 W. Larkspur Rd, #115 Brimwell, FL 33990
  </div>
  <div class="promo abs">
    <svg width="14" height="12" viewBox="0 0 14 12"><rect x="1" y="1" width="12" height="10" rx="1" fill="none" stroke="#777"/><path d="M1 4h12" stroke="#777"/></svg>
    Free Dental Screening <b>From Nov 10 &amp; 20</b>
  </div>
</div>

<header class="site-header">
  <div class="logo abs"><span class="brand-dot"></span><span class="brand-name">The Tooth Corner of Brimwell</span></div>
  <nav class="main-nav abs">
    <span class="active">HOME</span>
    <span class="caret">ABOUT US</span>
    <span class="caret">SERVICES</span>
    <span class="caret">TESTIMONIALS</span>
    <span class="caret">CONTACT US</span>
  </nav>
  <div class="phone abs">
    <svg width="15" height="15" viewBox="0 0 24 24"><path d="M6.6 10.8a15 15 0 0 0 6.6 6.6l2.2-2.2a1 1 0 0 1 1-.25 11.4 11.4 0 0 0 3.6.57 1 1 0 0 1 1 1V20a1 1 0 0 1-1 1A17 17 0 0 1 3 4a1 1 0 0 1 1-1h3.5a1 1 0 0 1 1 1c0 1.25.2 2.45.57 3.57a1 1 0 0 1-.25 1z" fill="#333"/></svg>
    213-555-0147
  </div>
</header>

<section class="hero">
  <div class="photo abs" role="img" aria-label="Photo of a smiling dentist in a white coat in a bright clinic"></div>
  <div class="welcome abs">Welcome to</div>
  <h1 class="brand-name abs">The Tooth Corner</h1>
  <div class="brand-sub abs">of Brimwell</div>
  <div class="tagline abs">BEAUTIFUL SMILE<br>BEGINS HERE</div>
  <a class="btn abs">Fix Appointment</a>
</section>

<section class="about">
  <div class="logo abs"><span class="brand-dot"></span><div><small>Welcome to the</small><span class="brand-name">The Tooth Corner of Brimwell</span></div></div>
  <div class="bio abs">
    <p>Our clinic has cared for local families for many years. We offer gentle checkups, clear advice and modern treatment in a calm and friendly office. Every visit starts with listening to you and ends with a plan you understand.</p>
    <p>Dr. Ortega studied dentistry with a focus on family care and keeps learning new methods each year. She speaks English and Spanish and welcomes patients of every age.</p>
  </div>
  <a class="btn abs">Read more</a>
  <div class="hours-card abs">
    <div class="photo abs" role="img" aria-label="Portrait photo of the dentist"></div>
    <h3 class="abs">Opening Hours</h3>
    <table>
      <tr><td>Weekdays</td><td>8.00-20.00</td></tr>
      <tr><td>Saturday</td><td>9.30-17.30</td></tr>
      <tr><td>Sunday</td><td>9.30-15.00</td></tr>
    </table>
    <div class="name-bar abs">Dr. Elena Marisol Ortega, DDS</div>
  </div>
</section>

<section class="banner">
  <div class="photo abs" role="img" aria-label="Photo of a smiling patient with curly hair in a dental office"></div>
  <h2 class="heading abs">Make your<br><strong>Smile brighter</strong></h2>
  <div class="call-box abs">
    <div class="label">CALL TO MAKE AN APPOINTMENT</div>
    <div class="number">1-888-555-0192</div>
  </div>
  <div class="touch abs">Keep in Touch with us</div>
  <div class="social abs"><span></span><span></span><span></span></div>
</section>

<section class="services">
  <h2 class="section-title abs">Our <em>Services</em></h2>
  <div class="sub abs">DENTAL TREATMENTS</div>
  <svg class="divider abs" viewBox="0 0 420 20"><line x1="0" y1="10" x2="190" y2="10" stroke="#ccc"/><line x1="230" y1="10" x2="420" y2="10" stroke="#ccc"/><path d="M203 4c3-2 6-2 7 0 1-2 4-2 7 0 2 3 0 7-1 10s-2 4-3 1l-3-3-3 3c-1 3-2 2-3-1s-3-7-1-10z" fill="var(--green)"/></svg>
  <p class="intro abs">We provide complete dental care for the whole family under one roof. From routine cleanings to full smile makeovers, our team uses safe, modern tools and clear pricing so you always know what to expect. Walk-in emergency visits are welcome during opening hours.</p>
  <div class="service abs" style="left:125px">
    <div class="circle"><svg width="60" height="60" viewBox="0 0 60 60"><circle cx="30" cy="30" r="26" fill="none" stroke="#fff" stroke-width="3"/><path d="M20 22c4-4 8-3 10-1 2-2 6-3 10 1 3 5 0 12-2 18-1 4-3 4-4 0l-4-5-4 5c-1 4-3 4-4 0-2-6-5-13-2-18z" fill="none" stroke="#fff" stroke-width="3"/></svg></div>
    <h4>PREVENTIVE DENTISTRY</h4><p>Cleaning | Dental Exams<br>Dental Xrays | Oral hygiene</p>
  </div>
  <div class="service abs" style="left:380px">
    <div class="circle"><svg width="60" height="60" viewBox="0 0 60 60"><path d="M14 14c7-6 12-4 16-1 4-3 9-5 16 1 5 8 0 20-3 30-2 6-5 6-6 0l-7-8-7 8c-1 6-4 6-6 0-3-10-8-22-3-30z" fill="none" stroke="#fff" stroke-width="3.5"/></svg></div>
    <h4>RESTORATIVE DENTISTRY</h4><p>Dental Implants | Child Dentistry<br>Braces | Bridges | Crowns<br>Whitening</p>
  </div>
  <div class="service abs" style="left:600px">
    <div class="circle"><svg width="60" height="60" viewBox="0 0 60 60"><path d="M16 10h28c0 8-4 12-14 12S16 18 16 10z" fill="#fff"/><path d="M22 26h16M23 32h14M24 38h12M26 44h8M28 50h4" stroke="#fff" stroke-width="3"/></svg></div>
    <h4>COSMETIC DENTISTRY</h4><p>Cleaning | Dental Exams<br>Dental Xrays | Oral hygiene</p>
  </div>
  <div class="service abs" style="left:825px">
    <div class="circle"><svg width="60" height="60" viewBox="0 0 60 60"><rect x="10" y="24" width="40" height="26" rx="3" fill="none" stroke="#fff" stroke-width="3"/><path d="M30 30v14M23 37h14" stroke="#fff" stroke-width="3"/><path d="M22 24v-6h16v6" fill="none" stroke="#fff" stroke-width="3"/></svg></div>
    <h4>EMERGENCY</h4><p>Cleaning | Dental Exams<br>Dental Xrays | Oral hygiene</p>
  </div>
</section>

<section class="appointment">
  <h2 class="section-title abs">Request an appointment</h2>
  <div class="sub abs">GET APPOINTMENT IN FOUR STEPS</div>
  <div class="steps-line abs"></div>
  <div class="step abs" style="left:135px"><div class="box"><svg width="26" height="26" viewBox="0 0 26 26"><rect x="3" y="3" width="20" height="20" rx="2" fill="var(--blue)"/><path d="M13 8v10M8 13h10" stroke="#fff" stroke-width="3"/></svg></div>SEARCH HOSPITAL</div>
  <div class="step abs" style="left:340px"><div class="box"><svg width="26" height="26" viewBox="0 0 26 26"><circle cx="11" cy="11" r="7" fill="none" stroke="var(--blue)" stroke-width="3"/><path d="M16 16l7 7" stroke="var(--blue)" stroke-width="3"/></svg></div>SEARCH DOCTOR</div>
  <div class="step abs" style="left:620px"><div class="box"><svg width="26" height="26" viewBox="0 0 26 26"><rect x="5" y="3" width="16" height="20" rx="1" fill="none" stroke="var(--blue)" stroke-width="2.5"/><path d="M9 9h8M9 13h8M9 17h5" stroke="var(--blue)" stroke-width="2"/></svg></div>FILL OUT FORM</div>
  <div class="step abs" style="left:845px"><div class="box"><svg width="26" height="26" viewBox="0 0 26 26"><circle cx="13" cy="13" r="11" fill="var(--blue)"/><path d="M7 13l4 4 8-8" fill="none" stroke="#fff" stroke-width="3"/></svg></div>APPOINTMENT DONE</div>

  <form class="form-card abs">
    <div class="field" style="left:92px;top:95px;width:375px">Your Name</div>
    <div class="field" style="left:505px;top:95px;width:375px">Select Service</div>
    <div class="field" style="left:92px;top:165px;width:375px">Your Email</div>
    <div class="field" style="left:505px;top:165px;width:200px">Select Date</div>
    <div class="field" style="left:720px;top:165px;width:160px">Select Time</div>
    <div class="field" style="left:92px;top:235px;width:375px">Your Phone number</div>
    <div class="field" style="left:505px;top:235px;width:375px">Your Message Here</div>
    <div class="note abs">* Required Field</div>
    <a class="btn abs">BOOK APPOINTMENT</a>
  </form>
</section>

<section class="testimonials">
  <h2 class="section-title abs">What Our Clients Say</h2>
  <svg class="abs" style="left:585px;top:118px" width="30" height="22" viewBox="0 0 30 22"><path d="M8 3c3-2 6-2 7 0 1-2 4-2 7 0 2 3 0 8-1 12s-2 4-3 1l-3-3-3 3c-1 3-2 3-3-1S6 6 8 3z" fill="#fff"/></svg>
  <p class="quote abs">The whole team made my family feel at home from the first visit. The office is clean, the staff is kind and Dr. Ortega explained every step before starting. My kids now look forward to their checkups, and booking an appointment online takes just a minute. We are happy to have found a dentist so close to home.</p>
  <div class="author abs">MARISSA</div>
  <div class="avatars abs" role="img" aria-label="Small round photos of four happy clients"><span></span><span></span><span></span><span></span></div>
</section>

<section class="map" role="img" aria-label="Street map showing the clinic location in Brimwell"></section>

<footer class="site-footer">
  <div class="logo abs"><span class="brand-dot"></span><div class="brand-name">The Tooth Corner of Brimwell</div></div>
  <div class="habla abs">SE HABLA<br>ESPAÑOL</div>
  <div class="footer-contact abs">
    <h5>CONTACT INFORMATION</h5>
    <div class="addr">
      <svg width="18" height="26" viewBox="0 0 10 14"><path d="M5 0a5 5 0 0 0-5 5c0 4 5 9 5 9s5-5 5-9a5 5 0 0 0-5-5zm0 7a2 2 0 1 1 0-4 2 2 0 0 1 0 4z" fill="var(--green)"/></svg>
      <div><b>ADDRESS</b><p>Dental Clinic at Brimwell now open<br>4120 W. Larkspur Rd,<br>#115 Brimwell, FL 33990</p></div>
    </div>
    <div class="call">Call to Make an appointment</div>
    <div class="num">1-888-555-0192</div>
  </div>
  <div class="footer-doctor abs">
    <h5>LOOKING FOR A GOOD DOCTOR</h5>
    <p>Friendly family dentistry with same week visits, clear prices and care for every smile.</p>
    <a class="btn">MAKE APPOINTMENT</a>
    <div class="touch">Keep in Touch with us</div>
    <div class="social"><span></span><span></span><span></span></div>
    <div class="insurance"><svg width="18" height="18" viewBox="0 0 18 18"><path d="M2 9l5 5 9-10" fill="none" stroke="var(--green)" stroke-width="3"/></svg>All insurance accepted</div>
  </div>
  <div class="footer-bottom">© 2018 thetoothcornerofbrimwell.com. All Right Reserved</div>
</footer>

</body>
</html>
```